Updated Business Card for Optometry Practice

We're a growing optometry practice that is moving to a beautiful new office and we want to update our business card. We just updated our logo so the new card should reflect the new logo. Our practice continually invests in state of the art instruments to help us provide eye care that is thorough, comfortable, efficient and educational.

I've attached our current card and logo. You can reference this for the information I would like on the card. The tag line on the back is "We're changing the way you see."

Upon completion of this project we will need (amongst other formats) Photoshop files of the card so I can change employee names to print cards for each employee.

```html
<!DOCTYPE html>
<html lang="en">
<head>
<meta charset="utf-8">
<title>Northgate Family Eyecare – Business Card</title>
<link href="https://fonts.googleapis.com/css2?family=Montserrat:wght@400;500;600;700&display=swap" rel="stylesheet">
<style>
  :root{
    --stage:#8d8d8d;
    --navy:#17284d;
    --navy-deep:#122142;
    --gold:#d8ab2b;
    --gold-soft:rgba(216,171,43,.16);
    --paper:#ffffff;
    --ink:#1a2a50;
  }
  *{box-sizing:border-box;margin:0;padding:0}
  html,body{width:1200px;height:900px;overflow:hidden}
  body{background:var(--stage);font-family:"Montserrat",sans-serif;position:relative}
  .card{position:absolute;width:560px;height:320px;border-radius:3px;box-shadow:0 6px 18px rgba(0,0,0,.25);overflow:hidden}
  .card-front{left:80px;top:110px;background:linear-gradient(135deg,var(--navy-deep),var(--navy) 60%,#1c3160)}
  .card-back{left:560px;top:460px;background:var(--paper)}

  .front-glow{position:absolute;left:120px;top:20px;width:320px;height:280px;background:radial-gradient(ellipse at center,rgba(255,255,255,.06),rgba(255,255,255,0) 70%)}
  .front-brand{position:absolute;left:0;right:0;top:105px;text-align:center;color:var(--paper)}
  .front-brand .brand-name{font-size:46px;font-weight:500;letter-spacing:1px;line-height:1.1}
  .front-brand .brand-sub{font-size:22px;font-weight:500;letter-spacing:10px;margin-top:10px}
  .tagline{position:absolute;left:0;right:0;bottom:46px;text-align:center;color:var(--gold);font-weight:600;font-size:13px}

  .back-glow{position:absolute;left:-60px;top:60px;width:320px;height:320px;background:radial-gradient(ellipse at center,var(--gold-soft),rgba(216,171,43,0) 68%)}
  .back-brand{position:absolute;left:250px;top:36px;color:var(--ink)}
  .back-brand .brand-name{font-size:34px;font-weight:500;letter-spacing:.5px;line-height:1}
  .back-brand .brand-sub{display:inline-block;margin-top:6px;background:var(--navy);color:var(--paper);font-size:13px;font-weight:500;letter-spacing:6px;padding:3px 14px 3px 16px}
  .contact{position:absolute;left:264px;top:130px;color:var(--ink)}
  .person-name{font-size:19px;font-weight:700}
  .person-role{font-size:12px;font-weight:500;margin-top:1px}
  .address{font-size:12px;font-weight:500;margin-top:16px;line-height:1.4}
  .lines{list-style:none;margin-top:12px;font-size:12px;font-weight:500}
  .lines li{display:flex;align-items:center;gap:8px;margin-bottom:5px}
  .lines svg{width:12px;height:12px;flex:none}
</style>
</head>
<body>
  <section class="card card-front" aria-label="Card front">
    <div class="front-glow" role="img" aria-label="Faint brand mark area"></div>
    <div class="front-brand">
      <div class="brand-name">Northgate</div>
      <div class="brand-sub">Family Eyecare</div>
    </div>
    <p class="tagline">We're changing the way you see</p>
  </section>

  <section class="card card-back" aria-label="Card back">
    <div class="back-glow" role="img" aria-label="Large faint brand mark area"></div>
    <div class="back-brand">
      <div class="brand-name">Northgate</div>
      <div class="brand-sub">Family Eyecare</div>
    </div>
    <div class="contact">
      <p class="person-name">Daniel Marsh, OD</p>
      <p class="person-role">Optometrist</p>
      <p class="address">2870 Alder Ridge Blvd<br>Millbrook, MO 63012</p>
      <ul class="lines">
        <li><svg viewBox="0 0 24 24"><path fill="#1a2a50" d="M6.6 10.8a15 15 0 0 0 6.6 6.6l2.2-2.2a1 1 0 0 1 1-.25 11.4 11.4 0 0 0 3.6.57 1 1 0 0 1 1 1V20a1 1 0 0 1-1 1A17 17 0 0 1 3 4a1 1 0 0 1 1-1h3.5a1 1 0 0 1 1 1c0 1.25.2 2.45.57 3.6a1 1 0 0 1-.25 1z"/></svg>(555) 014-2290</li>
        <li><svg viewBox="0 0 24 24"><path fill="#1a2a50" d="M2 5h20v2l-10 7L2 7z"/><path fill="#1a2a50" d="M2 9l10 7 10-7v10H2z"/></svg>dan@northgateeyecare.com</li>
        <li><svg viewBox="0 0 24 24"><circle cx="12" cy="12" r="9" fill="none" stroke="#1a2a50" stroke-width="2"/><path d="M3 12h18M12 3c3 3 3 15 0 18M12 3c-3 3-3 15 0 18" fill="none" stroke="#1a2a50" stroke-width="1.6"/></svg>northgateeyecare.com</li>
      </ul>
    </div>
  </section>
</body>
</html>
```